Yacht, Boats, Watersports company needs a redesign of business card

Hello Designers!
We are a Boat dealership company that sells fun in the water, we sell boats, Yachts, Kayaks and also yacht WaterSport toys. We are looking to redesign our business cards in to something a little bit more sophisticated. in a way that we can make better use of our company colors. I'm attaching a zipped file containing the company 3 sets of company logo which one is an horizontal another one is a vertical and also a chromed 3d logo. Also is included two set of business cards that we use and also some designs that i think it's interesting. We use PMS 2026c Orange and PMS 7687C Blue. I would like to see at least two different options with the orange as accent and also using blue as an accent color. It's really important for the business cards to have a font option and size that is legible to most people. Our current website is www.corvellamarine.com. Please visit if you want to have a better feeling of the Boat dealership
You can send Single sided or double side options. We are now using single sided but we may be open for a double side option if we really like the design.
Target Market(s)
Marine, boat sales, yacht sales, water toys sales/
Contact Information for Business Card
Name: Dale Pritchett
Address: 718 West Halden Lane,
Selwyn Cove, FL 33019
Phone: 555-382-7146
Fax: 555-382-7139
Cell: 555-451-8320
Email: dale@corvellamarine.com
Website: corvellamarine.com
Requirements
Must have
- the current information of the business card provided.
logo
use the PMS Colors
Nice to have
- a touch of elegance and sophistication but simple
Should not have
- should not have any typography that is hard to read, the card should be simple but yet sophisticated.

```html
<!DOCTYPE html>
<html lang="en">
<head>
<meta charset="utf-8">
<title>Corvella Marine — Business Card Options</title>
<link rel="stylesheet" href="https://fonts.googleapis.com/css2?family=Montserrat:wght@400;600;700&display=swap">
<style>
:root{
  --blue:#0f4f9a;
  --blue-deep:#0a3470;
  --blue-light:#2a78c8;
  --orange:#f26a21;
  --white:#ffffff;
  --paper:#f4f4f4;
  --stage:#e4e5e7;
  --ink:#2b2f36;
}
*{box-sizing:border-box;margin:0;padding:0}
html,body{width:855px;height:1200px;overflow:hidden}
body{background:var(--stage);font-family:"Montserrat",sans-serif;position:relative}
.card{position:absolute;overflow:hidden;box-shadow:0 2px 5px rgba(0,0,0,.18)}
.card.h{width:365px;height:194px}
.card.v{width:199px;height:370px}
.col-l{left:51px}.col-r{left:439px}
.water{position:absolute;inset:0;background:radial-gradient(circle at 30% 40%,var(--blue-light),var(--blue) 45%,var(--blue-deep))}
.burst{position:absolute;inset:0;background:radial-gradient(circle at 50% 45%,#2f86d6,var(--blue) 40%,var(--blue-deep))}
.brand{position:absolute;display:flex;align-items:center;gap:6px;font-weight:700;letter-spacing:.5px;white-space:nowrap}
.brand .dot{width:22px;height:22px;border-radius:50%;border:2px solid currentColor;flex:none}
.brand.light{color:var(--white)}
.brand.dark{color:var(--blue)}
.name{position:absolute;font-weight:700;letter-spacing:.6px;white-space:nowrap}
.contacts{position:absolute;list-style:none;font-size:6.5px;line-height:1}
.contacts li{display:flex;align-items:center;gap:6px;margin-bottom:5px;white-space:nowrap}
.ico{width:11px;height:11px;border-radius:50%;background:var(--white);flex:none}
.contacts.dark .ico{width:6px;height:6px;background:var(--orange)}
.address{position:absolute;font-size:6.5px;line-height:1.5;white-space:nowrap}
.pin{display:block;width:8px;height:10px;margin-bottom:4px}
.stripe{position:absolute;background:var(--orange)}
</style>
</head>
<body>

<!-- Option 1 front -->
<section class="card h col-l" style="top:57px">
  <div class="water" role="img" aria-label="Deep blue water texture background"></div>
  <div class="brand light" style="left:30px;top:38px;font-size:10px"><span class="dot"></span>CORVELLA MARINE</div>
  <div class="address" style="left:40px;top:130px;color:var(--white)">
    <svg class="pin" viewBox="0 0 8 10"><path d="M4 0a4 4 0 0 1 4 4c0 3-4 6-4 6S0 7 0 4a4 4 0 0 1 4-4z" fill="#fff"/></svg>
    718 West Halden Lane,<br>Selwyn Cove, FL 33019
  </div>
  <div class="stripe" style="left:205px;top:0;width:14px;height:194px"></div>
  <div class="name" style="left:238px;top:18px;font-size:11px;color:var(--white)">DALE PRITCHETT</div>
  <ul class="contacts" style="left:232px;top:44px;color:var(--white)">
    <li><span class="ico"></span>555-382-7146</li>
    <li><span class="ico"></span>555-382-7139</li>
    <li><span class="ico"></span>555-451-8320</li>
    <li><span class="ico"></span>dale@corvellamarine.com</li>
    <li><span class="ico"></span>corvellamarine.com</li>
    <li><span class="ico"></span>www.corvellamarine.com</li>
  </ul>
</section>

<!-- Option 1 back -->
<section class="card h col-r" style="top:57px">
  <div class="burst" role="img" aria-label="Blue radial light burst background"></div>
  <div class="brand light" style="left:50%;top:50%;transform:translate(-50%,-50%);font-size:11px;flex-direction:column;gap:8px"><span class="dot" style="width:30px;height:30px"></span>CORVELLA MARINE</div>
</section>

<!-- Option 2 front -->
<section class="card h col-l" style="top:274px;background:var(--white)">
  <div class="brand dark" style="left:16px;top:14px;font-size:10px"><span class="dot" style="color:var(--orange)"></span>CORVELLA MARINE</div>
  <div class="stripe" style="left:0;top:66px;width:365px;height:26px;clip-path:polygon(35% 0,100% 0,100% 100%,30% 100%)"></div>
  <div style="position:absolute;left:0;top:66px;width:115px;height:26px;background:var(--blue);clip-path:polygon(0 0,100% 0,88% 100%,0 100%)"></div>
  <div class="name" style="left:190px;top:74px;font-size:11px;color:var(--white)">DALE PRITCHETT</div>
  <ul class="contacts dark" style="left:16px;top:112px;color:var(--ink)">
    <li><span class="ico"></span>555-382-7146</li>
    <li><span class="ico"></span>555-382-7139</li>
    <li><span class="ico"></span>555-451-8320</li>
    <li><span class="ico"></span>dale@corvellamarine.com</li>
    <li><span class="ico"></span>corvellamarine.com</li>
  </ul>
  <div class="address" style="left:240px;top:145px;color:var(--ink)">718 West Halden Lane,<br>Selwyn Cove, FL 33019</div>
</section>

<!-- Option 2 back -->
<section class="card h col-r" style="top:274px;background:var(--paper)">
  <div class="brand dark" style="left:50%;top:50%;transform:translate(-50%,-50%);font-size:12px"><span class="dot" style="width:30px;height:30px;color:var(--orange)"></span>CORVELLA MARINE</div>
</section>

<!-- Option 3 front -->
<section class="card h col-l" style="top:547px">
  <div class="water" role="img" aria-label="Marbled blue water texture background"></div>
  <div class="brand light" style="left:30px;top:38px;font-size:10px"><span class="dot"></span>CORVELLA MARINE</div>
  <div class="address" style="left:40px;top:130px;color:var(--white)">
    <svg class="pin" viewBox="0 0 8 10"><path d="M4 0a4 4 0 0 1 4 4c0 3-4 6-4 6S0 7 0 4a4 4 0 0 1 4-4z" fill="#fff"/></svg>
    718 West Halden Lane,<br>Selwyn Cove, FL 33019
  </div>
  <div class="stripe" style="left:205px;top:12px;width:16px;height:16px"></div>
  <div class="name" style="left:232px;top:15px;font-size:11px;color:var(--white)">DALE PRITCHETT</div>
  <ul class="contacts" style="left:232px;top:44px;color:var(--white)">
    <li><span class="ico"></span>555-382-7146</li>
    <li><span class="ico"></span>555-382-7139</li>
    <li><span class="ico"></span>555-451-8320</li>
    <li><span class="ico"></span>dale@corvellamarine.com</li>
    <li><span class="ico"></span>corvellamarine.com</li>
    <li><span class="ico"></span>www.corvellamarine.com</li>
  </ul>
</section>

<!-- Option 3 back -->
<section class="card h col-r" style="top:547px">
  <div class="water" role="img" aria-label="Marbled blue water texture background"></div>
  <div class="brand light" style="left:50%;top:50%;transform:translate(-50%,-50%);font-size:11px;flex-direction:column;gap:8px"><span class="dot" style="width:30px;height:30px"></span>CORVELLA MARINE</div>
</section>

<!-- Option 4 back (vertical) -->
<section class="card v" style="left:217px;top:804px">
  <div class="water" role="img" aria-label="Swirling blue water texture background"></div>
  <div class="brand light" style="left:50%;top:40px;transform:translateX(-50%);font-size:9px;flex-direction:column;gap:6px"><span class="dot" style="width:24px;height:24px"></span>CORVELLA MARINE</div>
</section>

<!-- Option 4 front (vertical) -->
<section class="card v" style="left:442px;top:804px;background:var(--white);text-align:center">
  <div style="position:absolute;left:50%;top:28px;transform:translateX(-50%);width:56px;height:56px;border-radius:50%;border:4px solid var(--orange)"></div>
  <div class="name" style="left:0;right:0;top:108px;font-size:12px;color:var(--ink)">DALE PRITCHETT</div>
  <div class="address" style="left:0;right:0;top:140px;color:var(--ink);line-height:2.6">
    718 West Halden Lane,<br>Selwyn Cove, FL 33019<br>555-382-7146<br>555-382-7139<br>555-451-8320<br>dale@corvellamarine.com<br>corvellamarine.com
  </div>
</section>

</body>
</html>
```